WORDPRESS WEB DESIGN PROJECT-DESIGN & DEVELOP

OUR BUSINESS
Bright Harbour Consulting provides effective project controls and management solutions for construction projects in Australia and Overseas. We provide services to both large multinational companies and smaller privately owned businesses. Our knowledge and expertise assist clients to effectively plan and manage their construction projects or project portfolios. Our focus is to provide your business with the tools, solutions and strategies necessary to deliver projects on time and within budget.

WHY WE ARE RE-BRANDING OUR WEBSITE
Our existing website design is not effective at promoting our business. We require a fresh, new, innovative approach to effectively market our business brand. Our new website will have the same look and feed as our newly developed business brochure.

DESIGN
Our new website will have the same look and feed as our business brochure. This website will be developed in Word press; a customized theme is required. The graphic design and images will enhance the written content; any graphics need to be developed in Photoshop as this is the software we use. A horizontal navigation menu will be implemented but must blend into the design and not be contained in a colour band. The webpage itself needs to span the entire viewable screen and must not look like an A4 piece of paper on a colored background. Additional design comments have been attached to this project as " website contents" word doc.

WEDSITES I LIKE THE LOOK OF
www.example-tarvion.com (very professional, similar color scheme)
www.example-quellory.com ( Good design, background made the website pop)
www.example-brimwoodfloorcare.com.au (clean,tidy,sharp images)
www.example-velantis.com ( the look was simple but effective)
http://www.example-norvik.com

STYLE
We require a stylish, clean and easy to navigate website, with fresh, exciting and engaging imagery. Our website design needs to be modern, clean and sleek.

WRITTEN CONTENT
New written content for each page is provided with this project, there is 50% less content in this project than the original website.

QUALITY
High resolution images and photos will be used to promote an overall quality, professional look and feel.

FUNCTIONALITY
The design needs to be easily updated and editable. The person updating the webpage content and images does not know coding, so the theme will need to be able to interact with plugins. All design components need to be optimized for indexing on major search engines e.g. Firefox, internet explorer, Google and safari.

ICONS
I will require icon links to Email, Facebook and LinkedIn, but not for twitter, Gmail or live feeds.

MENU
1.Home
2.Services
3.Benefits
4.Management
5.Planning
6.Optimization
7.Industry
8.Software
9.Contact us
10.Recruitment

TARGET AUDIENCE
Corporate Clients in all industry’s sectors
Supporting clients in
★OIL & Gas
★Iron Ore
★Coal
★New Industries
★Building and Construction
★Rail
★Civil
★Manufacturing
★Petrochemical
★Telecommunications

THE WINNER WILL PROVIDE
1. Wordpress theme with design.
2. List of plugins needed to meet requirements or design.
3. All images used in design.
4. Any custom php, javascript, or css files needed for the design.
5. List of core wordpress files customized as part of the design.
6. Any source files for custom images or design work (psd)

ATTACHMENTS
The following items will be attached to this project
1. Business logo
2. Icon images
3. Business Brochure PDF
4. Business brochure cover page psd file
5. Content required in each webpage

DESIGN AND DEVELOP
This project is to design and develop a word press website. In respect that the chosen designer may not be able to provide the development, 2 places of $400 each have been offered (1st for the design aspect, and 2nd for the development). The winning designer will receive $800 if both design and development have been achieved.

PROJECT CHANGES

The projects budget has increased from $600 to $800

Completion date has extended by 7 day.

Requirements
Should not have
• This design must have not appear out-dated or cluttered
Please do not provide any designs that look like our old website.

```html
<!DOCTYPE html>
<html lang="en">
<head>
<meta charset="utf-8">
<title>Bright Harbour Consulting</title>
<link rel="stylesheet" href="https://fonts.googleapis.com/css2?family=Arimo:wght@400;700&family=Tinos&display=swap">
<style>
:root{
  --black:#070707;
  --red:#e0141b;
  --deep-red:#8a0508;
  --yellow:#ffd200;
  --white:#ffffff;
  --panel:rgba(214,214,214,0.82);
  --dark-box:rgba(60,60,60,0.88);
  --footer:#9a9a9a;
  --label-bg:rgba(0,0,0,0.88);
  --text:#111111;
}
*{margin:0;padding:0;box-sizing:border-box}
html,body{width:1200px;height:1051px;overflow:hidden}
body{position:relative;font-family:"Arimo",Arial,sans-serif;color:var(--text);
  background:linear-gradient(180deg,#6f7173 0%,#9c9d9f 30%,#8d8f92 60%,#5b5e62 100%)}
.backdrop{position:absolute;inset:59px 0 62px 0;
  background:radial-gradient(ellipse at 12% 55%,rgba(255,255,255,.25),transparent 40%),
  radial-gradient(ellipse at 92% 40%,rgba(255,255,255,.3),transparent 35%),
  linear-gradient(180deg,#8a8c8f 0%,#b5b6b7 45%,#6d7074 100%)}
.topbar{position:absolute;left:0;top:0;width:1200px;height:59px;background:var(--black)}
.topbar .email{position:absolute;right:213px;top:21px;color:var(--white);font-size:16px}
.topbar .divider{position:absolute;left:1004px;top:17px;width:1px;height:26px;background:#444}
.topbar .phone{position:absolute;left:1020px;top:20px;color:var(--red);font-size:17px;font-weight:700;letter-spacing:.5px}
.brand{position:absolute;left:147px;top:92px;display:flex;align-items:center;gap:14px}
.brand .mark{width:46px;height:46px;background:var(--red)}
.brand .name{font-size:33px;font-weight:700;color:var(--black);letter-spacing:-.5px;line-height:1}
.brand .tagline{font-size:11.5px;font-weight:700;color:var(--black);margin-top:6px}
.social{position:absolute;left:967px;top:115px;display:flex;gap:9px}
.social span{width:37px;height:34px;background:linear-gradient(#5a5a5a,#1d1d1d);border:1px solid #888;display:block}
.social svg{display:block;margin:8px auto 0}
.panel{position:absolute;left:129px;top:185px;width:940px;height:804px;background:var(--panel)}
.nav{position:absolute;left:146px;top:197px;display:flex;list-style:none}
.nav li{font-size:16.5px;color:var(--black);padding:0 10px;border-left:2px solid var(--red);line-height:26px;white-space:nowrap}
.nav li:first-child{border-left:none;padding-left:0}
.nav li.serif{font-family:"Tinos","Times New Roman",serif;padding-right:0}
.slider{position:absolute;left:148px;top:237px;width:903px;height:390px}
.welcome{position:absolute;left:148px;top:257px;width:903px;height:116px;
  background:linear-gradient(90deg,#3d0103 0%,#7a0407 40%,#6a0205 70%,#2a0001 100%)}
.welcome h1{position:absolute;left:19px;top:10px;color:var(--yellow);font-size:45px;font-weight:700;letter-spacing:.5px}
.welcome h2{position:absolute;left:23px;top:62px;color:var(--white);font-size:32px;font-weight:700}
.dots{position:absolute;right:22px;top:90px;display:flex;gap:4px}
.dots i{width:7px;height:7px;border-radius:50%;background:#8a8a8a;display:block}
.dots i.on{background:#e8e8e8}
.intro{position:absolute;left:148px;top:659px;width:293px;height:85px;background:var(--red);
  padding:6px 8px;font-size:14.3px;font-weight:700;line-height:16.5px;color:var(--black)}
.about{position:absolute;left:148px;top:744px;width:293px;height:205px;background:var(--dark-box);
  padding:8px 8px;font-size:14.2px;line-height:17.5px;color:var(--white)}
.tile{position:absolute;width:139px;height:138px}
.tile .pic{position:absolute;inset:0}
.tile .label{position:absolute;left:0;bottom:0;width:100%;height:27px;background:var(--label-bg);
  color:var(--white);font-size:14.5px;font-weight:700;text-align:center;line-height:27px}
.tile .label.muted{color:#c9c9c9;font-weight:400}
.footer{position:absolute;left:0;top:989px;width:1200px;height:62px;background:var(--footer);
  color:var(--white);font-size:14px;font-weight:700;text-align:center;line-height:52px}
</style>
</head>
<body>
<div class="backdrop" role="img" aria-label="Night view of a lit petrochemical refinery"></div>

<header class="topbar">
  <span class="email">sam.reid@brightharbourconsulting.example</span>
  <span class="divider"></span>
  <span class="phone">+61 0400 112 233</span>
</header>

<div class="brand">
  <span class="mark"></span>
  <div>
    <div class="name">BRIGHT HARBOUR CONSULTING</div>
    <div class="tagline">Providing Effective Project Controls and Management Solutions</div>
  </div>
</div>

<div class="social">
  <span aria-label="Email"><svg width="22" height="16" viewBox="0 0 22 16"><rect x="1" y="1" width="20" height="14" fill="none" stroke="#fff" stroke-width="2"/><path d="M1 1l10 8 10-8" fill="none" stroke="#fff" stroke-width="2"/></svg></span>
  <span aria-label="Social profile link"></span>
</div>

<div class="panel"></div>

<ul class="nav">
  <li>Home</li><li>Services</li><li>Benefits</li><li>Management</li><li>Planning</li><li>Optimisation</li><li>Industry</li><li>Software</li><li>Contact us</li><li class="serif">Recruitment</li>
</ul>

<svg class="slider" viewBox="0 0 903 390" role="img" aria-label="Refinery towers and storage tank lit at night">
  <defs>
    <linearGradient id="scene" x1="0" y1="0" x2="0" y2="1">
      <stop offset="0" stop-color="#3a3d44"/>
      <stop offset=".6" stop-color="#5a5c60"/>
      <stop offset="1" stop-color="#2a2520"/>
    </linearGradient>
    <linearGradient id="swoosh" x1="0" y1="0" x2="0" y2="1">
      <stop offset="0" stop-color="#ff2a22"/>
      <stop offset="1" stop-color="#a8070b"/>
    </linearGradient>
  </defs>
  <rect x="0" y="0" width="903" height="390" fill="#d4d4d4"/>
  <path d="M0 0H903V220Q460 420 0 220Z" fill="url(#scene)"/>
  <path d="M0 215Q460 410 903 215V238Q460 430 0 238Z" fill="url(#swoosh)"/>
  <path d="M0 238Q460 430 903 238V252Q460 425 0 252Z" fill="#ffffff" opacity=".75"/>
</svg>

<section class="welcome">
  <h1>WELCOME TO</h1>
  <h2>BRIGHT HARBOUR CONSULTING</h2>
  <div class="dots"><i></i><i></i><i class="on"></i><i></i><i></i></div>
</section>

<p class="intro">Bright Harbour Consulting provides effective project controls and management solutions for construction projects in Australia and Overseas.</p>
<p class="about">We provide services to both large multinational companies and smaller privately owned businesses. Our knowledge and expertise assist clients to effectively plan and manage their construction projects or project portfolios. Our focus is to provide your business with the tools, solutions and strategies necessary to deliver projects on time and within budget. We provide short or long term support, depending on your needs</p>

<div class="tile" style="left:456px;top:659px"><div class="pic" role="img" aria-label="Electrical switchgear in blue light" style="background:linear-gradient(135deg,#0d2a6b,#3a6fc0 60%,#0a1a40)"></div><div class="label">Services</div></div>
<div class="tile" style="left:608px;top:659px"><div class="pic" role="img" aria-label="Welder working amid sparks" style="background:linear-gradient(160deg,#2a1a10,#b0601a 55%,#3a2010)"></div><div class="label">Benefits</div></div>
<div class="tile" style="left:760px;top:659px"><div class="pic" role="img" aria-label="Power plant chimneys at dusk" style="background:linear-gradient(180deg,#1c3a78,#5a6a90 55%,#c07a30)"></div><div class="label muted">Management</div></div>
<div class="tile" style="left:912px;top:659px"><div class="pic" role="img" aria-label="Industrial building at sunset" style="background:linear-gradient(180deg,#2a2040,#7a3a2a 50%,#c06a20 75%,#3a1a10)"></div><div class="label">planning</div></div>

<div class="tile" style="left:456px;top:811px"><div class="pic" role="img" aria-label="Refinery towers on a grey day" style="background:linear-gradient(180deg,#8a8a6a,#6a6a50 60%,#3a3a2a)"></div><div class="label muted">Optimisation</div></div>
<div class="tile" style="left:608px;top:811px"><div class="pic" role="img" aria-label="Pipelines stretching to the horizon" style="background:linear-gradient(180deg,#1a3a80,#6a88b0 45%,#9aa4b0)"></div><div class="label">Industry</div></div>
<div class="tile" style="left:760px;top:811px"><div class="pic" role="img" aria-label="Close-up of project schedule printout" style="background:linear-gradient(135deg,#e06a20,#f0a060 45%,#3a7ad0)"></div><div class="label">Software</div></div>
<div class="tile" style="left:912px;top:811px"><div class="pic" role="img" aria-label="Site workers in hard hats" style="background:linear-gradient(180deg,#7ab0e0,#c0d8f0 50%,#c02a20 80%,#e0c040)"></div><div class="label">Recruitment</div></div>

<footer class="footer">Copyright © 2013 Bright Harbour Consulting. All rights reserved</footer>
</body>
</html>
```